Torven Medical needs bold attention catching website for healthcare professionals(target)

I need a hero page as well as a products and about page for a website of mine. I specialize in orthopedic instruments . Specifically bone drills and saws. This whole company was founded to bring superb quality highly discounted medical instruments. Specifically bone drills, bone saws, k-wires and pins. Two main points should be cost savings and superior quality.

Target Market(s)

healthcare professionals Surgeons and hospital material managers

Number of Pages Required

3 page

Font styles to use
Serif

Colors

Designer to choose colors to be used in the design.

Requirements
Must have
• colors should match logo design

```html
<!DOCTYPE html>
<html lang="en">
<head>
<meta charset="utf-8">
<title>Torven Medical — Orthopedic Instruments</title>
<link href="https://fonts.googleapis.com/css2?family=Crimson+Text:wght@400;600;700&family=Lato:wght@400;700&display=swap" rel="stylesheet">
<style>
:root{
  --orange:#f47c20;
  --orange-light:#f9a25a;
  --orange-deep:#e8650f;
  --navy:#2f3f52;
  --ink:#222;
  --body:#555;
  --muted:#888;
  --line:#e2e2e2;
  --paper:#fff;
  --card:#f6f6f6;
}
*{margin:0;padding:0;box-sizing:border-box}
html,body{width:1200px;height:3382px;overflow:hidden;background:var(--paper)}
body{position:relative;font-family:"Lato",sans-serif;color:var(--body)}
.abs{position:absolute}
.serif{font-family:"Crimson Text",serif}
a{color:inherit;text-decoration:none}

/* header */
.brand{left:95px;top:42px;display:flex;align-items:center;gap:10px;font-family:"Crimson Text",serif;font-size:30px;color:var(--orange);font-weight:600}
.brand .dot{width:14px;height:14px;border-radius:50%;background:var(--orange)}
.topbar{right:85px;top:14px;display:flex;gap:34px;font-size:12px;color:#666}
.topbar span{display:flex;align-items:center;gap:6px}
.header-rule{left:328px;top:44px;width:872px;height:1px;background:var(--line)}
.nav{left:625px;top:67px;display:flex;gap:31px;font-size:12px;color:#555}
.login{left:1019px;top:67px;font-size:12px;color:var(--orange);display:flex;gap:18px;align-items:center}

/* hero */
.hero-band{left:0;top:188px;width:981px;height:532px;background:linear-gradient(135deg,var(--orange-deep),var(--orange) 45%,var(--orange-light))}
.hero-photo{left:331px;top:105px;width:869px;height:534px;background:linear-gradient(160deg,#51617a,#33435c 55%,#6b4a4a);opacity:.95}
.hero-tint{left:331px;top:188px;width:293px;height:451px;background:rgba(244,124,32,.35)}
.hero-block{left:624px;top:227px;width:357px;height:587px;background:rgba(244,124,32,.88)}
.hero-card{left:737px;top:341px;width:370px;height:298px;background:#fff;padding:10px}
.hero-card div{width:100%;height:100%;background:linear-gradient(135deg,#e8ebef,#c9ced6 50%,#f5b066)}
.hero-kicker{left:95px;top:306px;font-size:38px;color:#fff}
.hero-title{left:94px;top:350px;font-size:76px;line-height:66px;font-weight:700;color:#fff;letter-spacing:1px}
.hero-link{left:93px;top:514px;font-size:18px;color:#fff;border-bottom:2px solid #fff;padding-bottom:2px}

/* features */
.feature-frame{border:1px dashed #ddd;border-bottom:none;height:150px;top:803px}
.feature{top:813px;width:481px;height:147px;background:#fff;border:1px solid #ccc;padding:33px 38px}
.feature h3{font-family:"Crimson Text",serif;font-weight:400;font-size:28px;color:var(--ink)}
.feature p{font-size:11px;line-height:15px;margin-top:14px;width:300px;color:#666}
.feature svg{position:absolute;right:34px;top:32px}
.hex{background:var(--orange);background-image:radial-gradient(circle at 30% 40%,rgba(255,255,255,.15),transparent 60%)}

/* about */
.about-title{left:95px;top:1172px;font-size:42px;color:var(--ink)}
.about-rule{left:95px;top:1234px;width:489px;height:1px;background:var(--orange)}
.about-text{left:92px;top:1274px;width:430px;font-size:12px;line-height:19.5px;color:#444}
.more{font-size:11px;color:var(--orange)}
.about-photo{left:601px;top:1094px;width:506px;height:398px;background:linear-gradient(150deg,#3d8d8a,#2d6a78 50%,#b98a6a)}

/* products */
.products-band{left:0;top:1615px;width:981px;height:378px;background:linear-gradient(120deg,var(--orange-light),var(--orange) 50%,var(--orange-deep))}
.products-label{left:1015px;top:1620px;width:76px;font-size:60px;color:#e6e6e6;writing-mode:vertical-rl;letter-spacing:2px}
.product{top:1694px;width:179px}
.product .pic{height:193px}
.product .tag{margin-left:-21px;width:147px;height:33px;background:var(--navy);color:#fff;font-family:"Crimson Text",serif;font-size:17px;padding:6px 0 0 23px}

/* blog */
.blog-title{left:0;width:1200px;text-align:center;top:2090px;font-size:40px;color:var(--ink)}
.post{top:2160px;width:311px;height:425px;background:var(--card);border:1px solid #e4e4e4}
.post .pic{height:210px;position:relative}
.post .chev{display:block}
.post .date{position:absolute;left:0;top:0;width:47px;height:59px;background:#2a2a2a;color:#fff;text-align:center;font-size:18px;padding-top:8px;line-height:16px}
.post .date small{display:block;font-size:10px}
.post h4{font-family:"Crimson Text",serif;font-weight:400;font-size:16px;line-height:20px;color:var(--ink);margin:14px 28px 0}
.post p{font-size:11px;line-height:15.5px;color:#777;margin:22px 28px 0}
.post p span{color:var(--orange)}

/* newsletter */
.news{left:0;top:2665px;width:1200px;height:302px}
.news-title{left:0;width:1200px;text-align:center;top:2724px;font-size:34px;font-weight:700;color:#fff}
.news-rule{left:552px;top:2782px;width:96px;height:2px;background:#fff}
.news-text{left:0;width:1200px;text-align:center;top:2822px;font-size:13px;color:#fff}
.news-input{left:302px;top:2853px;width:595px;height:47px;background:#fff;border-radius:24px;padding:15px 28px;font-size:11px;color:#444}
.news-input svg{position:absolute;right:28px;top:12px}

/* footer */
.foot-about{left:93px;top:3103px;width:290px;font-size:11px;line-height:17px;color:#555}
.socials{left:93px;top:3214px;display:flex;gap:4px}
.socials i{width:24px;height:24px;border-radius:50%;background:var(--orange)}
.foot-h{top:3040px;font-family:"Crimson Text",serif;font-size:19px;font-weight:600;color:var(--ink)}
.foot-list{top:3103px;list-style:none;font-size:11px;line-height:22.5px;color:#555}
.foot-list li::before{content:"|";margin-right:15px;color:#888}
.contact{left:929px;top:3103px;font-size:11px;color:#555}
.contact div{display:flex;gap:14px;margin-bottom:16px;line-height:14px}
.foot-rule{left:0;top:3302px;width:1200px;height:1px;background:var(--line)}
.copy{left:93px;top:3336px;font-size:11px;color:#333}
.legal{right:93px;top:3336px;font-size:11px;color:#333}
</style>
</head>
<body>

<!-- header -->
<div class="abs brand"><span class="dot"></span>Torven Medical</div>
<div class="abs topbar">
  <span><svg width="12" height="12" viewBox="0 0 24 24"><path fill="#f47c20" d="M6.6 10.8a15 15 0 006.6 6.6l2.2-2.2c.3-.3.7-.4 1-.2 1.1.4 2.3.6 3.6.6.6 0 1 .4 1 1V20c0 .6-.4 1-1 1A17 17 0 013 4c0-.6.4-1 1-1h3.5c.6 0 1 .4 1 1 0 1.3.2 2.5.6 3.6.1.3 0 .7-.2 1z"/></svg>555 0142 730</span>
  <span><b style="color:var(--orange);font-weight:400">@</b> info@torvenmedical.com</span>
  <span><svg width="12" height="12" viewBox="0 0 24 24"><path fill="#f47c20" d="M22 2L2 10l8 3 3 8z"/></svg>Store Location</span>
</div>
<div class="abs header-rule"></div>
<nav class="abs nav"><a>Home</a><a>About us</a><a>Products</a><a>Blog</a><a>Contact Us</a></nav>
<div class="abs login"><a>Login</a><span>|</span>
  <svg width="12" height="12" viewBox="0 0 24 24"><circle cx="10" cy="10" r="7" fill="none" stroke="#f47c20" stroke-width="3"/><path d="M15 15l6 6" stroke="#f47c20" stroke-width="3"/></svg></div>

<!-- hero -->
<div class="abs hero-band"></div>
<div class="abs hero-photo" role="img" aria-label="Surgeons in masks operating"></div>
<div class="abs hero-tint"></div>
<div class="abs hero-block"></div>
<div class="abs hero-card"><div role="img" aria-label="Two orthopedic pins on a folded geometric backdrop"></div></div>
<div class="abs hero-kicker serif">Torven Medical Specialize In</div>
<h1 class="abs hero-title serif">ORTHOPEDIC<br>INSTRUMENTS</h1>
<a class="abs hero-link">Read More About Us &rarr;</a>
<svg class="abs" style="left:1067px;top:667px" width="22" height="24" viewBox="0 0 22 24"><circle cx="11" cy="13" r="9" fill="none" stroke="#333" stroke-width="1.3"/><path d="M11 2v12M8 11l3 3 3-3" fill="none" stroke="#333" stroke-width="1.3"/></svg>

<!-- features -->
<div class="abs feature-frame" style="left:93px;width:491px"></div>
<div class="abs feature-frame" style="left:616px;width:491px"></div>
<div class="abs feature" style="left:93px">
  <h3>Cost Savings</h3>
  <p>Donec non justo et eros aliquam rhoncus at nec purus. Donec et hendrerit sem, ut convallis lorem.</p>
  <svg width="84" height="84" viewBox="0 0 84 84"><ellipse cx="38" cy="52" rx="30" ry="22" fill="#f47c20" stroke="#2f3f52" stroke-width="2.5"/><rect x="18" y="66" width="10" height="12" fill="#f47c20" stroke="#2f3f52" stroke-width="2.5"/><rect x="46" y="66" width="10" height="12" fill="#f47c20" stroke="#2f3f52" stroke-width="2.5"/><circle cx="50" cy="18" r="13" fill="#f47c20" stroke="#2f3f52" stroke-width="2.5"/><text x="50" y="24" font-size="16" text-anchor="middle" fill="#2f3f52" font-family="Lato" font-weight="700">$</text><circle cx="20" cy="46" r="2.5" fill="#2f3f52"/></svg>
</div>
<div class="abs feature" style="left:616px">
  <h3>Superior Quality</h3>
  <p>Donec non justo et eros aliquam rhoncus at nec purus. Donec et hendrerit sem, ut convallis lorem.</p>
  <svg width="78" height="78" viewBox="0 0 78 78"><circle cx="39" cy="39" r="37" fill="#f47c20"/><circle cx="39" cy="39" r="26" fill="none" stroke="#fff" stroke-width="3"/><path d="M27 47V32l7 6 5-8 5 8 7-6v15z" fill="none" stroke="#2f3f52" stroke-width="3" stroke-linejoin="round"/></svg>
</div>
<div class="abs hex" style="left:797px;top:960px;width:184px;height:115px" role="img" aria-label="Orange hexagon pattern"></div>

<!-- about -->
<h2 class="abs about-title serif" style="font-weight:400">About Torven Medical</h2>
<div class="abs about-rule"></div>
<p class="abs about-text">Hospitals are increasingly seeking ways to cut cost while continuing to deliver high quality medical care.  Torven Medical was created to offer hospitals and physicians high-quality products at a significantly lower cost. Torven Medical focus is on the orthopedic disposable market by providing quality generic products that are utilized to replace many legacy products that have low physician preference and are subject to 5%-10% annual unsustainable price increases.</p>
<a class="abs more" style="left:92px;top:1406px">Read More &rarr;</a>
<div class="abs about-photo" role="img" aria-label="Surgeon using a bone drill during an operation"></div>
<div class="abs hex" style="left:797px;top:1510px;width:184px;height:105px" role="img" aria-label="Orange hexagon pattern"></div>

<!-- products -->
<div class="abs products-band" role="img" aria-label="Orange tinted surgical instruments background"></div>
<div class="abs products-label serif">PRODUCTS</div>
<div class="abs product" style="left:117px"><div class="pic" style="background:linear-gradient(160deg,#e9e9e9,#f07a2a 60%,#3a3a3a)" role="img" aria-label="Orange cordless bone drill"></div><div class="tag">Bone Drills</div></div>
<div class="abs product" style="left:330px"><div class="pic" style="background:linear-gradient(160deg,#6b5a4a,#b58a5e 60%,#d7b48a)" role="img" aria-label="Bone saw bits on a wooden stand"></div><div class="tag">Bone Saws</div></div>
<div class="abs product" style="left:543px"><div class="pic" style="background:linear-gradient(160deg,#a88878,#c79a86 50%,#7c5a50)" role="img" aria-label="K-wire fixation on a hand"></div><div class="tag">K-Wires</div></div>
<div class="abs product" style="left:756px"><div class="pic" style="background:linear-gradient(180deg,#c9cdd2,#8a8070 50%,#e8e8e8)" role="img" aria-label="Surgical pins in a holder"></div><div class="tag">Pins</div></div>

<!-- blog -->
<h2 class="abs blog-title serif" style="font-weight:400">From Our Blog</h2>
<article class="abs post" style="left:93px">
  <div class="pic" style="background:linear-gradient(135deg,#eef1f3,#c9d3da 60%,#4b5866)" role="img" aria-label="Doctor with clipboard beside ultrasound equipment"><div class="date">23<small>DEC</small></div></div>
  <svg class="chev" width="311" height="22" viewBox="0 0 311 22"><path d="M0 0L155 22 311 0" fill="none" stroke="#f47c20" stroke-width="4"/></svg>
  <h4>Nullam metus purus, fermentum at nisi at, sollicitudin suscipit velit.</h4>
  <p>Aenean a congue leo. Duis mattis gravida turpis cursus fermentum. Sed nec erat non libero vestibulum auctor. In augue sapien, interdum at condimentum sed, varius vitae tortor. Aenean ornare accumsan posuere <span>[...]</span></p>
</article>
<article class="abs post" style="left:445px">
  <div class="pic" style="background:linear-gradient(135deg,#5d8fc4,#2f66a8 60%,#dfe6ee)" role="img" aria-label="Three smiling doctors in scrubs"><div class="date">23<small>DEC</small></div></div>
  <svg class="chev" width="311" height="22" viewBox="0 0 311 22"><path d="M0 0L155 22 311 0" fill="none" stroke="#f47c20" stroke-width="4"/></svg>
  <h4>Nullam metus purus, fermentum at nisi at, sollicitudin suscipit velit.</h4>
  <p>Aenean a congue leo. Duis mattis gravida turpis cursus fermentum. Sed nec erat non libero vestibulum auctor. In augue sapien, interdum at condimentum sed, varius vitae tortor. Aenean ornare accumsan posuere <span>[...]</span></p>
</article>
<article class="abs post" style="left:796px">
  <div class="pic" style="background:linear-gradient(135deg,#dfe8d6,#f2f2f2 55%,#c9ccd0)" role="img" aria-label="Doctor holding a tablet at a desk"><div class="date">23<small>DEC</small></div></div>
  <svg class="chev" width="311" height="22" viewBox="0 0 311 22"><path d="M0 0L155 22 311 0" fill="none" stroke="#f47c20" stroke-width="4"/></svg>
  <h4>Nullam metus purus, fermentum at nisi at, sollicitudin suscipit velit.</h4>
  <p>Aenean a congue leo. Duis mattis gravida turpis cursus fermentum. Sed nec erat non libero vestibulum auctor. In augue sapien, interdum at condimentum sed, varius vitae tortor. Aenean ornare accumsan posuere <span>[...]</span></p>
</article>

<!-- newsletter -->
<svg class="abs news" viewBox="0 0 1200 302" preserveAspectRatio="none">
  <defs><linearGradient id="ng" x1="0" y1="0" x2="1" y2="1"><stop offset="0" stop-color="#f26a12"/><stop offset=".5" stop-color="#f47c20"/><stop offset="1" stop-color="#f7954a"/></linearGradient></defs>
  <path d="M0 30L600 0 1200 30V302H0z" fill="url(#ng)"/>
</svg>
<h2 class="abs news-title serif">Join Our Newsletter</h2>
<div class="abs news-rule"></div>
<p class="abs news-text">Lorem ipsum dolor sit amet, consectetur adipiscing elit, sed do</p>
<div class="abs news-input">Enter Your Email Id
  <svg width="24" height="22" viewBox="0 0 24 22"><path d="M23 1L1 10l8 3 3 8z M23 1L9 13" fill="#2a2a2a" stroke="#2a2a2a" stroke-width="1.5" stroke-linejoin="round"/></svg></div>

<!-- footer -->
<div class="abs brand" style="top:3036px;font-size:26px"><span class="dot"></span>Torven Medical</div>
<p class="abs foot-about">Lorem ipsum dolor sit amet, consectetur adipiscing elit, sed do eiusmod tempor incididunt ut labore et dolore magna aliqua. Quis ipsum suspendisse ultrices gravida. Risus commodo viverra maecenas accumsan lacus vel facilisis.</p>
<div class="abs socials"><i></i><i></i><i></i><i></i></div>

<h4 class="abs foot-h" style="left:472px">Information</h4>
<ul class="abs foot-list" style="left:472px"><li>Home</li><li>About us</li><li>products</li><li>Information</li><li>Blog</li><li>Help &amp; Faq's</li><li>Contact Us</li></ul>
<h4 class="abs foot-h" style="left:681px">Info</h4>
<ul class="abs foot-list" style="left:681px"><li>Staff &amp; Contact</li><li>Privacy Policy</li><li>Product Terms &amp; Conditions</li><li>Returned Goods Policy</li><li>Terms of Use</li></ul>
<h4 class="abs foot-h" style="left:932px">Contact us</h4>
<div class="abs contact">
  <div><svg width="16" height="20" viewBox="0 0 16 20"><path d="M8 0a7 7 0 017 7c0 5-7 13-7 13S1 12 1 7a7 7 0 017-7z" fill="#f47c20"/><circle cx="8" cy="7" r="2.5" fill="#fff"/></svg><span>418 Harbor Park Lane FL<br>33410 USA</span></div>
  <div><svg width="16" height="16" viewBox="0 0 24 24"><path fill="#f47c20" d="M6.6 10.8a15 15 0 006.6 6.6l2.2-2.2c.3-.3.7-.4 1-.2 1.1.4 2.3.6 3.6.6.6 0 1 .4 1 1V20c0 .6-.4 1-1 1A17 17 0 013 4c0-.6.4-1 1-1h3.5c.6 0 1 .4 1 1 0 1.3.2 2.5.6 3.6.1.3 0 .7-.2 1z"/></svg><span>+1 555 0142 730</span></div>
  <div><b style="color:var(--orange);font-size:17px;font-weight:400;width:16px">@</b><span>info@torvenmedical.com</span></div>
</div>
<div class="abs foot-rule"></div>
<p class="abs copy">Copyright @ 2019, Torven Medical . All rights reserved.</p>
<p class="abs legal">Privac Policy &nbsp;&nbsp;&nbsp; | &nbsp;&nbsp;&nbsp; Terms &amp; Conditions</p>

</body>
</html>
```